Looking for fresh and exciting business card design that is simple and yet eye catching and impactfu

I am starting my own independent Marketing Communications consultancy with aim to service a small group of clients. Focus on aviation, travel and hospitality industries. Name of the consultancy is RVB BizLink or RVB Marketing Communications. Basic content of the card will be
RVB Marketing Communications / RVB BizLink
Greta Holm Vasquez
Email
Mobile
Website

Target Market(s)

Aviation, travel and hospitality industries

Industry/Entity Type

Travel

Contact Information for Business Card

Greta Holm Vasquez
Consultant
gretahkv@mailbrook.example
Mobile : +86 1502 846 2071
Skype: gretabluecanvas

Font styles to use
Sans Serif
Script

Requirements
Must have
• Professional look and feel.
Nice to have
• Fresh, contrast. I don't have a logo so using the company name to create a focal point.
Should not have
• Too many colors.

```html
<!DOCTYPE html>
<html lang="en">
<head>
<meta charset="utf-8">
<title>RVB BizLink – Business Card</title>
<link href="https://fonts.googleapis.com/css2?family=Open+Sans:ital,wght@0,400;0,600;0,700;1,400&display=swap" rel="stylesheet">
<style>
  :root {
    --navy: #27318f;
    --navy-soft: #323c9a;
    --ink: #4a4a4a;
    --grey-line: #c9c9c9;
    --paper: #ffffff;
    --backdrop: #e9e7e3;
  }
  * { margin: 0; padding: 0; box-sizing: border-box; }
  html, body { width: 1200px; height: 900px; overflow: hidden; }
  body {
    background: var(--backdrop);
    font-family: "Open Sans", Arial, sans-serif;
    position: relative;
  }
  .card {
    position: absolute;
    left: 290px;
    width: 620px;
    height: 354px;
    border-radius: 2px;
    box-shadow: 0 6px 18px rgba(0,0,0,0.18);
    overflow: hidden;
  }
  /* Back side */
  .card-back { top: 66px; background: var(--navy); }
  .card-back .pattern-field {
    position: absolute; inset: 0;
    background: var(--navy-soft);
  }
  .card-back .back-content {
    position: absolute; inset: 0;
    display: flex; flex-direction: column; align-items: center; justify-content: center;
    color: var(--paper);
  }
  .card-back .wordmark {
    font-size: 60px; font-weight: 400; letter-spacing: 4px; line-height: 1;
  }
  .card-back .website {
    margin-top: 18px;
    display: flex; align-items: center; gap: 10px;
    font-size: 14px; font-style: italic; letter-spacing: 1px;
  }
  .card-back .website .rule { width: 40px; height: 1px; background: var(--paper); opacity: .8; }

  /* Front side */
  .card-front { top: 478px; background: var(--paper); }
  .card-front .base-band {
    position: absolute; left: 0; right: 0; bottom: 0; height: 26px;
    background: var(--navy);
    border-top: 4px solid #eeeeee;
  }
  .card-front .brand {
    position: absolute; left: 48px; top: 112px;
    font-size: 40px; font-weight: 600; color: var(--navy);
    letter-spacing: 1px; line-height: 1;
  }
  .card-front .divider {
    position: absolute; left: 328px; top: 84px; width: 1px; height: 150px;
    background: linear-gradient(to bottom, transparent, var(--grey-line), transparent);
  }
  .card-front .contact { position: absolute; left: 356px; top: 92px; color: var(--ink); }
  .contact .person { font-size: 21px; font-weight: 700; color: var(--navy); line-height: 1.2; }
  .contact .role { font-size: 15px; margin-bottom: 12px; }
  .contact ul { list-style: none; }
  .contact li {
    display: flex; align-items: center; gap: 10px;
    font-size: 15px; line-height: 26px;
  }
  .contact li svg { width: 14px; height: 14px; flex: none; }
</style>
</head>
<body>

  <section class="card card-back" aria-label="Card back">
    <div class="pattern-field" role="img" aria-label="Faint repeating brand lettering pattern"></div>
    <div class="back-content">
      <div class="wordmark">RVB</div>
      <div class="website"><span class="rule"></span>www.rvbbizlink.example<span class="rule"></span></div>
    </div>
  </section>

  <section class="card card-front" aria-label="Card front">
    <div class="brand">RVB BizLink</div>
    <div class="divider"></div>
    <div class="contact">
      <div class="person">Greta Holm Vasquez</div>
      <div class="role">Consultant</div>
      <ul>
        <li>
          <svg viewBox="0 0 14 14" aria-hidden="true"><rect x="3" y="0.8" width="8" height="12.4" rx="1.5" fill="none" stroke="var(--navy)" stroke-width="1.4"/><circle cx="7" cy="11" r=".8" fill="var(--navy)"/></svg>
          +86 1502 846 2071
        </li>
        <li>
          <svg viewBox="0 0 14 14" aria-hidden="true"><circle cx="7" cy="7" r="6.5" fill="var(--navy)"/></svg>
          gretabluecanvas
        </li>
        <li>
          <svg viewBox="0 0 14 14" aria-hidden="true"><rect x="0.5" y="2.5" width="13" height="9" fill="var(--navy)"/><path d="M0.8 2.8 L7 8 L13.2 2.8" fill="none" stroke="#fff" stroke-width="1.1"/></svg>
          gretahkv@mailbrook.example
        </li>
      </ul>
    </div>
    <div class="base-band"></div>
  </section>

</body>
</html>
```